依頼詳細
依頼内容は以下の通りです。
・セミナーDMデザイン
・チラシで使用したイラストデータの提供(ホームページやパワーポイントに貼り付け)
・定期的なメンテナンス(2か月に1回程度、日時等の修正依頼予定)
⇒修正依頼する場合、時間的余裕を持って、別途プロジェクト登録します。

参考までに、これまで使用していたデザインと変更依頼内容を添付します。

現行デザインに固執しておりませんので、新たなデザインをお願いしたく思っております。

ご不明点等ございましたら、お問い合わせ下さい。

```html
<!DOCTYPE html>
<html lang="ja">
<head>
<meta charset="utf-8">
<title>コロナ融資借換＆資金調達セミナー</title>
<link rel="stylesheet" href="https://fonts.googleapis.com/css2?family=Noto+Sans+JP:wght@400;500;700;900&family=Roboto+Condensed:wght@700&display=swap">
<style>
:root{
  --blue:#1a6fc4;
  --blue-deep:#0d3f86;
  --blue-light:#d8ebfa;
  --sky:#eaf5fd;
  --orange:#f08a1c;
  --orange-deep:#d8620b;
  --yellow:#fff200;
  --ink:#1d2433;
  --grey:#6b7380;
  --white:#ffffff;
}
*{margin:0;padding:0;box-sizing:border-box}
html,body{width:846px;height:1200px;overflow:hidden;background:var(--white)}
body{font-family:"Noto Sans JP",sans-serif;color:var(--ink)}
.flyer{position:relative;width:846px;height:1200px;overflow:hidden;background:var(--white)}

.hero{position:absolute;left:0;top:0;width:846px;height:390px;
  background:linear-gradient(180deg,#f4f9fd 0%,#cfe4f4 55%,#a9c9e3 100%)}
.hero-photo{position:absolute;left:0;top:70px;width:846px;height:320px;
  background:radial-gradient(ellipse at 30% 80%,#8fb4d4 0%,rgba(143,180,212,0) 60%),linear-gradient(180deg,rgba(255,255,255,0) 0%,#b7d2e8 100%)}

.keywords{position:absolute;left:22px;top:16px;display:flex;gap:14px}
.keyword{width:148px;height:44px;border:2px solid var(--blue);border-radius:4px;background:var(--white);
  color:var(--blue);font-weight:900;font-size:24px;display:flex;align-items:center;justify-content:center;letter-spacing:.1em}

.steps{position:absolute;left:0;top:0;width:846px;height:390px}
.step{position:absolute;white-space:nowrap;background:linear-gradient(180deg,var(--orange),var(--orange-deep));color:var(--white);
  font-weight:900;border-radius:3px;padding:0 16px;display:flex;align-items:center;box-shadow:0 3px 6px rgba(0,0,0,.2)}
.step-1{left:300px;top:290px;height:38px;font-size:19px;color:var(--blue-deep);background:var(--white)}
.step-2{left:400px;top:222px;height:46px;font-size:26px}
.step-3{left:520px;top:140px;height:56px;font-size:32px}

.slogan{position:absolute;left:96px;top:372px;width:340px;height:34px;background:var(--blue-deep);
  transform:skewX(-18deg);display:flex;align-items:center;justify-content:center}
.slogan span{transform:skewX(18deg);color:var(--white);font-weight:900;font-size:20px;letter-spacing:.05em}

.title{position:absolute;left:0;width:846px;text-align:center;color:var(--blue);font-weight:900;letter-spacing:.01em;line-height:1;
  text-shadow:3px 3px 0 var(--white),0 4px 8px rgba(13,63,134,.25)}
.title-1{top:414px;font-size:74px}
.title-2{top:496px;font-size:76px}
.title .amp{color:var(--blue-deep)}

.dates{position:absolute;left:36px;top:602px;color:var(--blue);font-family:"Roboto Condensed","Noto Sans JP",sans-serif;font-weight:700;font-size:74px;line-height:1;display:flex;align-items:flex-end}
.dates small{font-size:16px;color:var(--white);background:var(--blue);padding:2px 5px;margin:0 10px 10px 6px;font-family:"Noto Sans JP",sans-serif}
.dates .dot{font-size:40px;margin:0 8px 16px 0}
.time{position:absolute;left:36px;top:680px;font-weight:900;font-size:38px;color:var(--blue-deep);display:flex;align-items:center}
.time small{font-size:13px;line-height:1.05;background:var(--blue-deep);color:var(--white);padding:3px 4px;margin-left:8px;text-align:center}

.info{position:absolute;left:36px;top:734px;width:470px}
.info-row{display:flex;align-items:baseline;font-size:21px;font-weight:700;margin-bottom:8px;white-space:nowrap}
.info-row .label{width:96px;flex:none}
.info-row .label::before{content:"■";color:var(--blue);margin-right:2px}
.info-sub{font-size:14px;font-weight:500;margin:-6px 0 8px 96px}
.badge{display:inline-block;font-size:12px;background:var(--orange);color:var(--white);padding:2px 6px;margin-left:8px}
.org{margin-left:96px;font-size:20px;font-weight:700;line-height:1.35}
.org small{font-size:13px;font-weight:500;display:block;line-height:1.5}
.org-mark{position:absolute;left:0;top:196px;width:80px;height:54px;border:1px solid #9aa3af;display:flex;align-items:center;justify-content:center;font-size:10px;color:var(--grey)}

.early{position:absolute;left:466px;top:620px;width:84px;height:84px;border-radius:50%;background:var(--blue);color:var(--white);
  font-weight:900;font-size:19px;line-height:1.15;display:flex;align-items:center;justify-content:center;text-align:center;border:3px solid var(--white);box-shadow:0 0 0 2px var(--blue)}
.stamp{position:absolute;left:588px;top:600px;font-weight:900;font-size:34px;color:var(--yellow);white-space:nowrap;
  -webkit-text-stroke:1.5px var(--orange-deep);transform:rotate(-12deg)}
.docs{position:absolute;left:552px;top:650px;width:270px;height:232px;border-radius:4px;
  background:linear-gradient(135deg,#bfe0f5 0%,#e9f0b0 60%,#f6f9e4 100%)}
.secret{position:absolute;left:546px;top:894px;width:282px;font-size:14px;font-weight:900;color:var(--blue-deep);white-space:nowrap;text-align:center}
.checks{position:absolute;left:556px;top:922px;list-style:none;font-size:13px;font-weight:500;line-height:1.7;white-space:nowrap}
.checks li::before{content:"✔";color:var(--blue);margin-right:4px}

.fax-note{position:absolute;left:36px;top:1044px;width:470px;font-size:14px;font-weight:500;text-align:center;
  border-top:1px dashed var(--grey);border-bottom:1px dashed var(--grey);padding:6px 0}

.search{position:absolute;left:540px;top:1052px;width:284px;height:36px;display:flex;border:2px solid var(--blue);background:var(--white)}
.search .query{flex:1;font-size:14px;font-weight:700;display:flex;align-items:center;padding-left:10px;white-space:nowrap}
.search .btn{width:60px;background:var(--blue);color:var(--white);font-size:15px;font-weight:700;display:flex;align-items:center;justify-content:center}
.url{position:absolute;left:540px;top:1096px;width:284px;text-align:center;font-size:13px;font-weight:500;color:var(--blue-deep)}

.deadline{position:absolute;left:0;top:1132px;width:846px;height:68px;background:var(--blue);color:var(--white);
  display:flex;align-items:center;justify-content:center;gap:16px;font-weight:700;font-size:18px;white-space:nowrap}
.deadline .tag{background:var(--white);color:var(--blue);padding:2px 10px;font-size:16px}
.deadline .date{background:var(--white);color:var(--ink);font-size:26px;font-weight:900;padding:0 14px}
.deadline .date.early-date{color:var(--orange-deep)}
</style>
</head>
<body>
<div class="flyer">
  <section class="hero">
    <div class="hero-photo" role="img" aria-label="上昇するグラフの上を歩くビジネスパーソンの写真"></div>
    <div class="keywords">
      <div class="keyword">円 安</div>
      <div class="keyword">物価高</div>
      <div class="keyword">人手不足</div>
      <div class="keyword">過剰債務</div>
      <div class="keyword">返済開始</div>
    </div>
    <div class="steps">
      <div class="step step-1">経営計画の策定</div>
      <div class="step step-2">資金繰り改善!!</div>
      <div class="step step-3">業績回復!!</div>
    </div>
  </section>

  <div class="slogan"><span>脱コロナ禍を実現する!!</span></div>
  <h1 class="title title-1">コロナ融資借換 <span class="amp">&amp;</span></h1>
  <p class="title title-2">資金調達セミナー</p>

  <div class="dates">4.19<small>WED</small><span class="dot">・</span>5.11<small>THU</small></div>
  <div class="time">14:00〜16:00<small>両日<br>とも</small></div>

  <div class="info">
    <div class="info-row"><span class="label">会　場</span>：洛央ビジネスセンター</div>
    <div class="info-sub">京都市中京区新町通錦小路上ル百足屋町12</div>
    <div class="info-row"><span class="label">受講料</span>：税込 10,000円<span class="badge">早期お申込特典あり</span></div>
    <div class="info-row"><span class="label">主　催</span>：経営革新等認定支援機関</div>
    <div class="org">有限会社 川村保険事務所
      <small>TEL 075-000-1234<br>〒604-0000 京都市中京区新町通 12</small>
    </div>
    <div class="org-mark">お問い合わせ先</div>
  </div>

  <div class="early">早期<br>特典</div>
  <div class="docs" role="img" aria-label="特典の小冊子と資料の表紙イメージ"></div>
  <div class="stamp">経営者必読!!</div>
  <p class="secret">会社と社長を守るサポートのヒミツとは</p>
  <ul class="checks">
    <li>銀行員が密かに確認したくなる資料</li>
    <li>経営計画書の書き方ひな形</li>
    <li>銀行交渉を有利に進めるガイド</li>
  </ul>

  <p class="fax-note">お申込は裏面の必要事項を記入の上、FAXにてお申込み下さい。</p>

  <div class="search"><span class="query">経営と財務の相談室　京都</span><span class="btn">検索</span></div>
  <p class="url">https://www.keiei-madoguchi.example/</p>

  <div class="deadline">
    <span class="tag">お申込期限</span><span class="date">4月7日 金</span>
    <span>お得な早期お申込期限</span><span class="date early-date">3月31日 金</span><span>まで</span>
  </div>
</div>
</body>
</html>
```